CD Design Cover - "Beyond the Orchard Gate"

I need a CD cover design. The original Album or CD was recorded in the early eighties. We are re-mastering it. It needs a fresh cover. The genre' is contemporary Christian music and the title of the album is "Beyond the Orchard Gate." This is referring to caring outside of the church walls. A picture of the solo artist could be integrated in the back design. It is not a good picture and does not have to be used. You would have to be creative in using it because of the quality. It does not have to be used at all. I also added some pictures I liked that could be used. I think I like the "Empty church opening" the best. Fits the theme perfectly.

Target Market(s)

30 years old and older.

Requirements
Must have
• Warmth
Nice to have
• I attached two pictures. One of an empty church and one with a reflection of a stain glass window on the wall. It would be nice to see some offerings using these pictures.
Should not have
• Not too churchy

```html
<!DOCTYPE html>
<html lang="en">
<head>
<meta charset="utf-8">
<title>Ray Hollander – Beyond the Orchard Gate</title>
<link href="https://fonts.googleapis.com/css2?family=Jost:wght@300;400;700&family=Raleway:wght@400;700&display=swap" rel="stylesheet">
<style>
  :root {
    --paper: #e8e4e1;
    --ink: #151312;
    --cover-dark: #0d0a09;
    --light-text: #f4f1ee;
    --warm-gold: #d9b02a;
    --warm-amber: #9a5a22;
    --glass-violet: #4a2f8c;
    --portrait-grey: #7d7a78;
  }
  * { margin: 0; padding: 0; box-sizing: border-box; }
  html, body { width: 1200px; height: 2400px; overflow: hidden; }
  body { background: var(--paper); position: relative; font-family: "Jost", sans-serif; color: var(--ink); }

  .header { position: absolute; top: 76px; left: 0; width: 1200px; text-align: center; }
  .header-artist { font-family: "Jost", sans-serif; font-weight: 300; font-size: 116px; line-height: 1; letter-spacing: 1px; }
  .header-artist b { font-weight: 700; }
  .header-title { font-family: "Jost", sans-serif; font-weight: 300; font-size: 58px; line-height: 1; margin-top: 8px; letter-spacing: 1px; }

  .cover { position: absolute; left: 142px; width: 914px; height: 910px; overflow: hidden; box-shadow: 0 16px 40px rgba(0,0,0,.45); background: var(--cover-dark); }
  .cover-front { top: 354px; }
  .cover-back { top: 1371px; }

  .light-photo { position: absolute; inset: 0; }
  .cover-front .light-photo {
    background:
      linear-gradient(115deg, var(--cover-dark) 0%, var(--cover-dark) 38%, var(--glass-violet) 46%, var(--warm-gold) 60%, var(--warm-amber) 80%, var(--warm-gold) 100%);
  }
  .cover-back .light-photo {
    background:
      linear-gradient(110deg, #2a1f16 0%, #7a4a20 22%, #4a3b24 40%, #1a1411 62%, var(--cover-dark) 100%);
  }

  .front-title { position: absolute; right: 64px; top: 60px; text-align: right; color: var(--light-text); font-weight: 300; font-size: 62px; line-height: 1.0; letter-spacing: 1px; }
  .front-artist { position: absolute; left: 58px; bottom: 50px; color: var(--light-text); font-weight: 400; font-size: 58px; line-height: 1; }
  .front-artist b { font-weight: 700; }

  .portrait { position: absolute; left: 98px; top: 90px; width: 160px; height: 160px; }

  .back-heading { position: absolute; right: 112px; top: 82px; text-align: right; color: var(--light-text); }
  .back-artist { font-weight: 400; font-size: 48px; line-height: 1; }
  .back-artist b { font-weight: 700; }
  .back-title { font-weight: 300; font-size: 38px; line-height: 1.02; margin-top: 10px; }

  .tracklist { position: absolute; right: 112px; top: 352px; list-style: none; text-align: right; font-family: "Raleway", sans-serif; font-size: 22px; line-height: 34.8px; color: var(--light-text); }

  .label { position: absolute; left: 440px; top: 765px; display: flex; align-items: center; gap: 34px; color: var(--light-text); }
  .label-address { text-align: center; font-family: "Raleway", sans-serif; font-size: 15px; line-height: 1.2; }
  .label-address strong { display: block; font-weight: 700; }
  .label-mark { display: flex; align-items: center; gap: 8px; font-family: "Raleway", sans-serif; font-weight: 700; font-size: 17px; }
  .label-mark-dot { width: 26px; height: 26px; border-radius: 50%; background: var(--light-text); }

  .credits { position: absolute; right: 112px; bottom: 30px; text-align: right; font-family: "Raleway", sans-serif; font-size: 15px; line-height: 1.35; color: var(--light-text); }
  .credits b { font-weight: 700; }
</style>
</head>
<body>
  <header class="header">
    <h1 class="header-artist"><b>Ray</b> Hollander</h1>
    <p class="header-title">BEYOND THE ORCHARD GATE</p>
  </header>

  <section class="cover cover-front">
    <div class="light-photo" role="img" aria-label="Photograph of a dim stone interior with coloured stained-glass light falling across the wall"></div>
    <h2 class="front-title">BEYOND<br>THE<br>ORCHARD<br>GATE</h2>
    <p class="front-artist"><b>RAY</b> HOLLANDER</p>
  </section>

  <section class="cover cover-back">
    <div class="light-photo" role="img" aria-label="Photograph of warm stained-glass light on a wall beneath a small window"></div>
    <svg class="portrait" viewBox="0 0 160 160" role="img" aria-label="Round portrait photo of the artist">
      <circle cx="80" cy="80" r="80" fill="var(--portrait-grey)"/>
    </svg>
    <div class="back-heading">
      <h2 class="back-artist"><b>Ray</b> Hollander</h2>
      <p class="back-title">BEYOND<br>THE ORCHARD<br>GATE</p>
    </div>
    <ol class="tracklist">
      <li>Morning Parcel</li>
      <li>Beyond the Orchard Gate</li>
      <li>Common Hands</li>
      <li>The Day the Rain Came Home</li>
      <li>Still Here</li>
      <li>One Last Tune Tonight</li>
      <li>Evening Psalm</li>
      <li>Back Where I Started</li>
      <li>Lantern on the Hill</li>
      <li>We'll Meet Again Someday</li>
    </ol>
    <div class="label">
      <p class="label-address"><strong>BLUESTEM RECORDS</strong>Millbrook, MO 65810</p>
      <div class="label-mark"><span class="label-mark-dot"></span><span>Bluestem</span></div>
    </div>
    <p class="credits"><b>Producer</b> June Harlow, <b>Engineered</b> Peter Kowalczyk, <b>Promoter</b> Ed Marsh,<br><b>Recorded at</b> Bluestem Studio.</p>
  </section>
</body>
</html>
```